Graphic to show our studio's values

We'd like to create a graphic of our values that can go onto fun gifts for our team in order to keep our values in front of all of us in a creative way. The graphic might go onto mugs, gift boxes, tote bags, etc. We are a growing interior architecture/design studio in Austin, TX. I encourage you to check out our website at www.vorrelandesign.com to get a sense of our vibe and culture. The graphic may or may not include the subtext to each value depending on how difficult it is to incorporate the subtext into a great design.

```html
<!DOCTYPE html>
<html lang="en">
<head>
<meta charset="utf-8">
<title>Our Values – Vorrelan Design</title>
<link href="https://fonts.googleapis.com/css2?family=Barlow+Semi+Condensed:wght@600;700&family=Poppins:wght@400;600&display=swap" rel="stylesheet">
<style>
  :root {
    --backdrop: #e6e7e9;
    --paper: #ffffff;
    --marble: #eceded;
    --lime: #b5cf4b;
    --charcoal: #58595b;
    --ink: #3a3b3d;
    --body: #4a4a4c;
  }
  * { margin: 0; padding: 0; box-sizing: border-box; }
  html, body { width: 1200px; height: 2589px; overflow: hidden; }
  body {
    background: var(--backdrop);
    position: relative;
    font-family: "Poppins", sans-serif;
  }
  .poster {
    position: absolute;
    left: 50px; top: 518px;
    width: 1100px; height: 1553px;
    background:
      radial-gradient(ellipse 60% 30% at 20% 15%, var(--marble), transparent 70%),
      radial-gradient(ellipse 50% 35% at 85% 70%, var(--marble), transparent 70%),
      var(--paper);
    box-shadow: 0 20px 50px rgba(0,0,0,.18);
    overflow: hidden;
  }
  .brand {
    position: absolute;
    top: 120px; left: 0; right: 0;
    display: flex; justify-content: center; align-items: center; gap: 26px;
  }
  .brand-square { width: 70px; height: 70px; background: var(--charcoal); }
  .brand-name {
    font-family: "Barlow Semi Condensed", sans-serif;
    font-weight: 700;
    font-size: 72px;
    letter-spacing: 6px;
    color: var(--charcoal);
  }
  .title {
    position: absolute;
    top: 345px; left: 0; right: 0;
    text-align: center;
    font-family: "Barlow Semi Condensed", sans-serif;
    font-weight: 700;
    font-size: 150px;
    line-height: 1;
    color: var(--ink);
  }
  .title .accent { color: var(--lime); }
  .values { position: absolute; left: 157px; top: 579px; width: 880px; }
  .value { position: relative; height: 201px; }
  .value-badge {
    position: absolute; left: 0; top: 0;
    width: 162px; height: 162px;
  }
  .value-badge::before {
    content: ""; position: absolute; inset: 0 0 0 0;
    border: 3px solid var(--ink);
    border-radius: 50% 0 50% 50%;
  }
  .value-badge::after {
    content: ""; position: absolute; left: 6px; top: 4px; right: -6px; bottom: -6px;
    background: var(--lime);
    border-radius: 50% 0 50% 50%;
    z-index: -1;
  }
  .value-badge { isolation: isolate; }
  .value-text { position: absolute; left: 246px; top: -8px; width: 600px; }
  .value-heading {
    font-family: "Barlow Semi Condensed", sans-serif;
    font-weight: 600;
    font-size: 38px;
    line-height: 1.1;
    color: var(--lime);
    margin-bottom: 4px;
  }
  .value-body { font-size: 26px; line-height: 31px; color: var(--body); }
  .site {
    position: absolute; top: 1424px; left: 0; right: 0;
    text-align: center;
    font-size: 35px;
    color: var(--body);
  }
  .site strong { color: var(--lime); font-weight: 600; }
  .foot-bar {
    position: absolute; bottom: 0; left: 431px;
    width: 238px; height: 19px;
    background: var(--lime);
  }
</style>
</head>
<body>
  <main class="poster">
    <header class="brand">
      <span class="brand-square"></span>
      <span class="brand-name">VORRELAN DESIGN</span>
    </header>

    <h1 class="title">OUR <span class="accent">VALUES</span></h1>

    <section class="values">
      <article class="value">
        <div class="value-badge" role="img" aria-label="Line icon of a brain above an open book"></div>
        <div class="value-text">
          <h2 class="value-heading">WE ARE LEARNERS</h2>
          <p class="value-body">We look for opportunities to learn from every project and interaction, and we share what we learn with each other.</p>
        </div>
      </article>
      <article class="value">
        <div class="value-badge" role="img" aria-label="Line icon of a thumbs-up hand"></div>
        <div class="value-text">
          <h2 class="value-heading">WE ARE POSITIVE</h2>
          <p class="value-body">We look for good, roll with the punches, have a sense of humor and celebrate each other</p>
        </div>
      </article>
      <article class="value">
        <div class="value-badge" role="img" aria-label="Line icon of a handshake with a shield"></div>
        <div class="value-text">
          <h2 class="value-heading">WE ARE TRUSTWORTHY</h2>
          <p class="value-body">We are our client’s advocate and trust worthy teamate.</p>
        </div>
      </article>
      <article class="value">
        <div class="value-badge" role="img" aria-label="Line icon of a monitor, laptop and phone"></div>
        <div class="value-text">
          <h2 class="value-heading">WE ARE RESPONSIVE</h2>
          <p class="value-body">We respond to our clients quickly and with enthusiasm as engaged teammates who are committed to partnering with them in accomplishing their goals.</p>
        </div>
      </article>
    </section>

    <p class="site">www.<strong>vorrelandesign</strong>.com</p>
    <div class="foot-bar"></div>
  </main>
</body>
</html>
```